Stationery Design Project

KT7 Staffing requires letterhead and business card designs for a company based in London. Just like the name, we're a management resourcing company, providing resources to third party companies. You can see www.kt7staffing-example.com for ideas on existing colour schemes and design concepts that have been implimented and agreed to. Ultimately the design should broadcast professionalism, safety and the concept of growth.

Target Market(s)

Financial institutes; friendly societies (All UK based)

Industry/Entity Type

Safety

Requirements
Must have
• Files produced should be print ready; and the text in them editable (eg address, name etc)

```html
<!DOCTYPE html>
<html lang="en">
<head>
<meta charset="utf-8">
<title>KT7 Staffing – Stationery</title>
<link rel="stylesheet" href="https://fonts.googleapis.com/css2?family=Carlito:ital,wght@0,400;0,700;1,400;1,700&display=swap">
<style>
  :root {
    --teal: #1a9aa6;
    --teal-light: #6fc0c9;
    --ink: #3b3b3b;
    --paper: #ffffff;
    --edge: #c9c9c9;
    --page: #ffffff;
  }
  * { box-sizing: border-box; margin: 0; padding: 0; }
  html, body {
    width: 1200px; height: 900px; overflow: hidden;
    background: var(--page);
    font-family: "Carlito", "Calibri", sans-serif;
  }
  .canvas { position: relative; width: 1200px; height: 900px; }

  .wordmark {
    font-family: "Carlito", "Calibri", sans-serif;
    font-weight: 700;
    color: var(--teal);
    letter-spacing: 0.5px;
    line-height: 1;
    white-space: nowrap;
  }

  /* Business card front */
  .card-front {
    position: absolute; left: 20px; top: 90px;
    width: 560px; height: 320px;
    background: var(--teal);
  }
  .card-front .wordmark {
    position: absolute; left: 296px; top: 148px;
    font-size: 38px; color: var(--paper);
  }

  /* Business card back */
  .card-back {
    position: absolute; left: 20px; top: 436px;
    width: 560px; height: 320px;
    background: var(--paper);
    border: 1px solid var(--edge);
  }
  .card-back .wordmark {
    position: absolute; left: 300px; top: 36px;
    font-size: 34px;
  }
  .holder { position: absolute; left: 30px; top: 116px; color: var(--teal); }
  .holder-name { font-size: 44px; line-height: 1; }
  .holder-role { font-size: 19px; color: var(--teal-light); margin-left: 20px; margin-top: -2px; }
  .card-rule {
    position: absolute; left: 144px; top: 90px;
    width: 1px; height: 168px; background: var(--teal-light);
  }
  .card-contact {
    position: absolute; left: 158px; top: 90px;
    list-style: none; font-size: 14.5px; line-height: 21px; color: var(--teal);
  }
  .card-contact .web { color: #5a8f96; }

  /* Letterhead */
  .letterhead {
    position: absolute; left: 596px; top: 20px;
    width: 580px; height: 860px;
    background: var(--paper);
    border: 1px solid var(--edge);
  }
  .letterhead .wordmark {
    position: absolute; left: 20px; top: 38px;
    font-size: 40px;
  }
  .letter-contact {
    position: absolute; right: 28px; top: 24px;
    list-style: none; text-align: right;
    font-size: 10.5px; line-height: 14px; color: var(--teal);
  }
  .letter-body {
    position: absolute; left: 18px; top: 214px; width: 540px;
    font-size: 9.5px; line-height: 12.2px; color: var(--ink);
  }
  .letter-body p { margin-bottom: 10px; }
  .letter-footer {
    position: absolute; left: 0; bottom: 0;
    width: 196px; height: 24px;
    background: var(--teal); color: var(--paper);
    font-size: 14px; font-weight: 700; font-style: italic;
    line-height: 24px; padding-left: 10px;
  }
</style>
</head>
<body>
<main class="canvas">

  <section class="card-front" aria-label="Business card front">
    <div class="wordmark">KT7 Staffing</div>
  </section>

  <section class="card-back" aria-label="Business card back">
    <div class="wordmark">KT7 Staffing</div>
    <div class="holder">
      <div class="holder-name">Name</div>
      <div class="holder-role">designation</div>
    </div>
    <div class="card-rule"></div>
    <ul class="card-contact">
      <li>Address: XXXXXXXXXXXXXX</li>
      <li>XXXXXXXXXXXXXXXXXXXXXXXXXX</li>
      <li>Landline: XXXXXXXX</li>
      <li>Mobile: XXX XXXXXX</li>
      <li>Email : XXXXXXXXXX</li>
      <li class="web">Website: www.kt7staffing-example.com</li>
    </ul>
  </section>

  <section class="letterhead" aria-label="Letterhead">
    <div class="wordmark">KT7 Staffing</div>
    <ul class="letter-contact">
      <li>Address: XXXXXXXXXXXX</li>
      <li>XXXXXXXXXXXXXXXXXXXXXX</li>
      <li>Email : XXXXXXXXX</li>
      <li>Website: www.kt7staffing-example.com</li>
      <li>Landline: XXXXXXX</li>
      <li>Mobile: XXX XXXXX</li>
    </ul>
    <div class="letter-body">
      <p>Dear Someone Somebody,</p>
      <p>Thank you for taking the time to meet with our team last week. We are pleased to confirm the staffing plan we discussed for your finance office. Our consultants will review each role and match it with skilled, vetted people. Every placement follows our safety checks and clear reporting from the first day.</p>
      <p>We will share weekly updates so that you can track progress with ease. Please let us know if any of the dates need to change. Our London office is open for calls and visits throughout the week. Our consultants will review each role and match it with skilled, vetted people.</p>
      <p>We are pleased to confirm the staffing plan we discussed for your finance office. Every placement follows our safety checks and clear reporting from the first day. We will share weekly updates so that you can track progress with ease. We look forward to building a long and steady partnership with you.</p>
      <p>Our London office is open for calls and visits throughout the week. Thank you for taking the time to meet with our team last week. Please let us know if any of the dates need to change. Every placement follows our safety checks and clear reporting from the first day.</p>
      <p>Our consultants will review each role and match it with skilled, vetted people. We look forward to building a long and steady partnership with you. We will share weekly updates so that you can track progress with ease. We are pleased to confirm the staffing plan we discussed for your finance office.</p>
      <p>Yours Sincerely,<br>ABC</p>
    </div>
    <div class="letter-footer">www.kt7staffing-example.com</div>
  </section>

</main>
</body>
</html>
```